Cannabis Dispensary Menu - Digital TV Display

This will be posted in a store on a tv to display all the products they have.
I have all the menu items added to a .psd file for you to work with already. I'm just looking for a good looking design thats also readable. The image size should be 1,920 x 1,080 pixels so that it displays well on a TV. I'd like categories/sub-categories to be separated from each other with some design elements. Another idea to save space would be to replace the CBD: and THC: labels with some kind of small icon that represents them

Target Market(s)

Cannabis consumers

Industry/Entity Type

Cannabis

Font styles to use
Sans Serif

Requirements
Must have
• The menu changes frequently so I will need a finished file I can edit.

```html
<!DOCTYPE html>
<html lang="en">
<head>
<meta charset="utf-8">
<title>Harbor Leaf Wellness – Menu Board</title>
<link href="https://fonts.googleapis.com/css2?family=Poppins:wght@600;700&family=Arimo:wght@400;700&display=swap" rel="stylesheet">
<style>
:root{
  --green:#2e5a50;
  --sage:#d3dad0;
  --sage-bar:#c5cdc1;
  --ink:#1a1a1a;
  --black:#000;
  --white:#fff;
  --bg:#ececec;
  --gold:#f0a11c;
}
*{margin:0;padding:0;box-sizing:border-box}
html,body{width:1011px;height:1200px;overflow:hidden;background:var(--bg)}
.stage{position:absolute;left:20px;top:327px;width:1520px;height:855px;transform:scale(0.6388);transform-origin:0 0;background:var(--white);font-family:Arimo,Arial,sans-serif;color:var(--ink);font-size:15.5px;line-height:19.5px;box-shadow:0 6px 16px rgba(0,0,0,.12)}
.abs{position:absolute}
.h-display{font-family:Poppins,Arial,sans-serif;font-weight:600;color:var(--green);line-height:1}
/* header */
.header{left:0;top:0;width:1520px;height:146px;background:var(--black);overflow:hidden}
.header-green{left:0;top:0;width:660px;height:146px}
.brand{left:55px;top:22px;font-family:Poppins,Arial,sans-serif;font-weight:700;font-size:38px;line-height:35px;color:var(--white)}
.brand span{display:block}
.brand .r{text-align:right}
.photo-bud{left:330px;top:0;width:330px;height:146px;background:radial-gradient(ellipse at 45% 50%,#8c9a4c 0%,#5e6f35 45%,rgba(46,90,80,0) 75%)}
.grade{left:698px;top:54px;font-family:Poppins,Arial,sans-serif;font-weight:700;font-size:38px;color:#d9d9d9;line-height:1}
.feature{top:14px;color:var(--white);font-size:16px;line-height:19.5px}
.feature h3{font-family:Poppins,Arial,sans-serif;font-weight:600;font-size:22px;line-height:26px}
.feature .row{display:grid;grid-template-columns:150px 40px}
.feature .row span:last-child{text-align:right}
.divider-v{left:1087px;top:20px;width:2px;height:118px;background:#fff}
.photo-oil{left:1300px;top:-10px;width:222px;height:160px;border-radius:50% 0 0 50%;background:radial-gradient(circle at 50% 45%,#ffd36a 0%,var(--gold) 55%,#c97a10 100%)}
/* columns */
.col-flower{left:0;top:146px;width:450px;height:709px;background:var(--white)}
.col-conc{left:450px;top:146px;width:450px;height:709px;background:var(--sage)}
.col-edibles{left:900px;top:146px;width:620px;height:709px;background:var(--white)}
.title{font-size:42px}
.bar{left:35px;width:388px;height:28px;background:var(--sage-bar);font-family:Poppins,Arial,sans-serif;font-weight:600;font-size:20px;line-height:28px;text-align:center}
.bar::before,.bar::after{content:"";position:absolute;top:8px;width:12px;height:12px;border-radius:50%;background:var(--green)}
.bar::before{left:18px}.bar::after{right:18px}
.bar small{font-family:Arimo,Arial,sans-serif;font-weight:400;font-size:15px}
.list4{left:36px;width:390px;display:grid;grid-template-columns:150px 55px 150px 35px}
.list4 .p{text-align:right}
.list4 .p1{text-align:left}
.center-text{text-align:center}
/* concentrates */
.cbar{left:25px;width:398px;height:31px}
.cbar .lbl{position:absolute;left:0;top:0;width:180px;height:31px;background:var(--white);font-family:Poppins,Arial,sans-serif;font-weight:600;font-size:20px;line-height:31px;padding-left:22px}
.cbar .price{position:absolute;right:0;top:0;width:242px;height:31px;background:var(--green);color:var(--white);font-size:16.5px;line-height:31px;padding-left:30px;clip-path:polygon(14px 0,100% 0,100% 100%,0 100%)}
.clist{left:31px;width:400px;display:grid;grid-template-columns:126px 79px 126px 60px}
.sub-h{font-family:Poppins,Arial,sans-serif;font-weight:600;font-size:21px}
.photo-gummies{left:0;top:631px;width:450px;height:78px;background:linear-gradient(90deg,#cfd3cd,#e4e6e2,#cfd3cd)}
/* edibles */
.elist{left:33px;width:280px;display:grid;grid-template-columns:212px 68px}
.hlist{left:337px;width:255px;display:grid;grid-template-columns:212px 43px}
.b{font-weight:700}
.photo-buds{left:320px;top:430px;width:300px;height:153px;background:radial-gradient(ellipse at 60% 70%,#a9a672 0%,#8a8a55 40%,rgba(255,255,255,0) 75%)}
.band{left:0;top:582px;width:620px;height:127px;background:var(--green);color:var(--white)}
.band h2{font-family:Poppins,Arial,sans-serif;font-weight:600;font-size:30px;line-height:1;color:var(--white)}
.coin{width:32px;height:32px;border-radius:50%;background:#e8e8e8;color:var(--green);font-family:Poppins,Arial,sans-serif;font-weight:700;font-size:14px;line-height:13px;text-align:center;padding-top:3px}
.band-div{left:387px;top:18px;width:2px;height:92px;background:#fff}
</style>
</head>
<body>
<main class="stage">
  <header class="abs header">
    <svg class="abs header-green" viewBox="0 0 660 146" aria-hidden="true"><polygon points="0,0 660,0 624,146 0,146" fill="#2e5a50"/><polygon points="652,0 664,0 628,146 616,146" fill="#9aa7a2"/></svg>
    <div class="abs brand"><span>Harbor</span><span>Leaf</span><span class="r">Wellness</span></div>
    <div class="abs photo-bud" role="img" aria-label="Close-up photo of a cannabis bud"></div>
    <div class="abs grade">AAAA+</div>
    <div class="abs feature" style="left:878px">
      <h3>Indica</h3>
      <div class="row"><span>Rose Pink Kush</span><span>28%</span></div>
      <div class="row"><span>3.5g</span><span>$25</span></div>
      <div class="row"><span>7g</span><span>$45</span></div>
      <div class="row"><span>14g</span><span>$85</span></div>
      <div class="row"><span>28g</span><span>$160</span></div>
    </div>
    <div class="abs divider-v"></div>
    <div class="abs feature" style="left:1115px">
      <h3>Hybrid</h3>
      <div class="row" style="grid-template-columns:105px 45px"><span>Harbor Kush</span><span>30%</span></div>
      <div class="row" style="grid-template-columns:105px 45px"><span>3.5g</span><span>$30</span></div>
      <div class="row" style="grid-template-columns:105px 45px"><span>7g</span><span>$50</span></div>
      <div class="row" style="grid-template-columns:105px 45px"><span>14g</span><span>$90</span></div>
      <div class="row" style="grid-template-columns:105px 45px"><span>28g</span><span>$160</span></div>
    </div>
    <div class="abs photo-oil" role="img" aria-label="Dish of golden cannabis oil capsules"></div>
  </header>

  <section class="abs col-flower">
    <h2 class="abs h-display title" style="left:35px;top:20px">Flower</h2>
    <div class="abs" style="left:338px;top:38px;font-size:20px">$50 oz's</div>
    <div class="abs bar" style="top:71px">Indica</div>
    <div class="abs list4" style="top:106px">
      <span>Blueberry</span><span class="p1">28%</span><span>Island Pink Kush</span><span class="p">24%</span>
      <span>Purple Vapor</span><span class="p1">27%</span><span>Green Crack</span><span class="p">24%</span>
      <span>Purple Kush</span><span class="p1">26%</span><span>White Rhino</span><span class="p">24%</span>
      <span>Ice Cream Cake</span><span class="p1">25%</span><span>Pink Kush</span><span class="p">21%</span>
      <span>Garlic Breath</span><span class="p1">24%</span><span>Grape Ape</span><span class="p">21%</span>
      <span>Master Kush</span><span class="p1">24%</span><span>Peyote Cookies</span><span class="p">22%</span>
      <span>Kushy Kush</span><span class="p1">24%</span><span>God Bud</span><span class="p">20%</span>
      <span>G13 Haze</span><span class="p1">24%</span><span></span><span></span>
    </div>
    <div class="abs bar" style="top:282px">Hybrid</div>
    <div class="abs list4" style="top:317px">
      <span>Campfire Cookies</span><span class="p1">28%</span><span>Miracle Alien</span><span class="p">22%</span>
      <span>Peanutbutter Breath</span><span class="p1">28%</span><span>Cookies</span><span></span>
      <span>Tangie</span><span class="p1">28%</span><span>Chem Dog</span><span class="p">29%</span>
      <span>White Widow</span><span class="p1">26%</span><span>Grape God</span><span class="p">20%</span>
      <span>Gelato</span><span class="p1">25%</span><span></span><span></span>
    </div>
    <div class="abs bar" style="top:435px">Sativa</div>
    <div class="abs list4" style="top:470px">
      <span>King Tut</span><span class="p1">33%</span><span>Pineapple Express</span><span class="p">25%</span>
      <span>Gamma Banner</span><span class="p1">29%</span><span></span><span></span>
    </div>
    <div class="abs bar" style="top:529px">CBD</div>
    <div class="abs" style="left:36px;top:565px">Candida</div>
    <div class="abs" style="left:250px;top:565px">CBD 20%</div>
    <div class="abs" style="left:325px;top:565px">THC 0.01%</div>
    <div class="abs bar" style="top:605px">Pre-Rolls <small>1-$5 or 2-$8</small></div>
    <div class="abs center-text" style="left:35px;top:640px;width:388px">JFK | Kushy Kush | Master Kush<br>Grape Ape | Green Crack | White Widow</div>
  </section>

  <section class="abs col-conc">
    <h2 class="abs h-display title" style="left:0;width:450px;text-align:center;top:20px">Concentrates</h2>
    <div class="abs cbar" style="top:71px"><div class="lbl">Live Resin</div><div class="price">1g - $30 or 5g - $100</div></div>
    <div class="abs clist" style="top:106px">
      <span>Blackberry</span><span>(Indica)</span><span>Gamma Banner</span><span>(Hybrid)</span>
      <span>Blue Dream</span><span>(Hybrid)</span><span>Energy Star</span><span>(Sativa)</span>
      <span>Gummy Bear</span><span>(Hybrid)</span><span></span><span></span>
    </div>
    <div class="abs cbar" style="top:190px"><div class="lbl">Shatter</div><div class="price">1g - $30 or 5g - $100</div></div>
    <div class="abs clist" style="top:225px">
      <span>Bubba Kush</span><span>(Indica)</span><span>Biscotti</span><span>(Hybrid)</span>
      <span>Death Star</span><span>(Indica)</span><span>Amnesia Haze</span><span>(Sativa)</span>
      <span>M.A.C. 1</span><span>(Hybrid)</span><span></span><span></span>
    </div>
    <div class="abs cbar" style="top:308px"><div class="lbl">Diamonds</div><div class="price">THCA 3.5g - $50</div></div>
    <div class="abs cbar" style="top:365px"><div class="lbl">Oil</div><div class="price">1g $30 | 3g $100 | 5g $200</div></div>
    <div class="abs center-text" style="left:0;width:450px;top:404px">Whole Plant Oil &nbsp;|&nbsp; Full Extract Cannabis Oil</div>
    <div class="abs sub-h" style="left:26px;top:446px">Hash</div>
    <div class="abs" style="left:139px;top:448px">Black Magic<br>1g - $15<br>5g - $50</div>
    <div class="abs" style="left:268px;top:448px">XXX<br>1g - $15<br>5g - $50</div>
    <div class="abs" style="left:364px;top:448px">XX<br>1g - $7<br>5g - $25</div>
    <div class="abs sub-h" style="left:26px;top:530px">Vapes</div>
    <div class="abs" style="left:139px;top:532px">Starlight 1g<br>Distillate - $35<br>Premium - $39</div>
    <div class="abs" style="left:268px;top:532px">Night Owl 1g<br>1 - $30 / 3 - $75</div>
    <div class="abs" style="left:268px;top:578px">Thunderclap 1g<br>1 - $30 / 3 - $75</div>
    <div class="abs photo-gummies" role="img" aria-label="Photo of translucent gummy bears"></div>
  </section>

  <section class="abs col-edibles">
    <h2 class="abs h-display title" style="left:33px;top:20px">Edibles</h2>
    <div class="abs elist" style="top:71px">
      <span>Shatter Chews 150mg</span><span>$20</span>
      <span>Shatter Bar 500mg</span><span>$30</span>
      <span>Gold Gang Gummies 500mg</span><span>$25</span>
      <span>Ridgeline Gummies</span><span></span>
      <span>500mg</span><span>$30</span>
      <span>3000mg</span><span>$50</span>
      <span>West Shore Gummies 600mg</span><span>$30</span>
      <span>Leaf Pop 60mg 1/3</span><span>$15/$40</span>
      <span>Canna Caps</span><span></span>
      <span>CBD: 13mg, THC: 145mg</span><span>$20</span>
      <span>Canna Sugar</span><span></span>
      <span>CBD: 15mg, THC: 50mg</span><span>$5</span>
      <span>Canna Cookies</span><span></span>
      <span>50mg</span><span>$5</span>
      <span>100mg</span><span>$10</span>
      <span>156mg</span><span>$15</span>
      <span>HLW Chocolates</span><span></span>
      <span>100mg</span><span>$10</span>
      <span>150mg</span><span>$15</span>
      <span>250mg</span><span>$25</span>
      <span>HLW Gummies</span><span></span>
      <span>20mg</span><span>$2</span>
      <span>100mg</span><span>$10</span>
      <span>200mg</span><span>$20</span>
      <span>300mg</span><span>$30</span>
    </div>
    <h2 class="abs h-display" style="left:337px;top:20px;font-size:33px;line-height:34px">Holistic Health<br>Essentials</h2>
    <div class="abs hlist" style="top:95px">
      <span class="b">Topical Cream</span><span></span>
      <span>THC: 500mg CBD: 50mg</span><span></span>
      <span>Small</span><span>$10</span>
      <span>Large</span><span>$25</span>
      <span>Bath Bombs CBD: 10mg</span><span></span>
      <span>THC: 50mg</span><span>$5</span>
      <span>THC: 100mg</span><span>$10</span>
      <span>THC: 150mg</span><span>$15</span>
      <span class="b">CBD Oil</span><span></span>
      <span>CBD: 1000mg</span><span>$40</span>
      <span>CBD: 5000mg</span><span>$200</span>
      <span>CBD VG Tincture</span><span></span>
      <span>CBD: 200mg THC: 60mg</span><span>$40</span>
      <span>VG Tincture</span><span></span>
      <span>CBD: 13mg THC: 450mg</span><span>$40</span>
      <span>CBD Patch CBD: 20mg</span><span>$20</span>
      <span>CBD Cream CBD: 3000mg</span><span>$20</span>
    </div>
    <div class="abs photo-buds" role="img" aria-label="Photo of dried cannabis buds"></div>
    <div class="abs band">
      <h2 class="abs" style="left:35px;top:16px">Pet Care</h2>
      <div class="abs" style="left:35px;top:50px">CBD Cat Treats<br>THC: 0.5mg<br>CBD: 5mg</div>
      <div class="abs coin" style="left:150px;top:60px">$<br>10</div>
      <div class="abs" style="left:206px;top:50px">CBD Dog Treats<br>THC: 2mg<br>CBD: 5.6mg</div>
      <div class="abs coin" style="left:322px;top:60px">$<br>10</div>
      <div class="abs band-div"></div>
      <h2 class="abs" style="left:418px;top:16px">Seasonal</h2>
      <div class="abs" style="left:418px;top:50px;width:180px;line-height:16.5px">
        <div style="display:grid;grid-template-columns:130px 40px"><span>Christmas THC<br>Crackers</span><span>$15</span></div>
        <div style="display:grid;grid-template-columns:130px 40px"><span>Christmas Edible<br>Advent Calendars</span><span>$80</span></div>
      </div>
    </div>
  </section>
</main>
</body>
</html>
```